Stationary for New Company

We need stationary designed for a new company. Details of the required stationary is attached.

The final version should be trendy, clean... only 2 colours (green + grey/black) and professional.

#1: Business Cards (design on 2 sides)
#2: Letterhead (word format)
#3: Cover Page and back cover for proposals
#4: Envelopes,
#5: Thank You card,
#6: Presentation Folder,
#7: Email signatures template (sample attached in word document)

Logo is attached. Logo can be reversed out (will attach once available). Logo can be stacked or horizontal (provided as horizontal).

Files need to be provided in ai + png format.

Target Market(s)

Business owners. More affluent.

Industry/Entity Type

Business

Requirements
Must have
• See brief

Font: Calibri
Should not have
• Photographs / stock photos

```html
<!DOCTYPE html>
<html lang="en">
<head>
<meta charset="utf-8">
<title>Thank You Card – Lanemark Insurance Brokers</title>
<link rel="stylesheet" href="https://fonts.googleapis.com/css2?family=Arimo:wght@400;700&family=Carlito:wght@400&family=Great+Vibes&display=swap">
<style>
  :root {
    --brand-green: #6a9a3d;
    --band-grey: #9a9a9a;
    --ink: #111111;
    --paper: #ffffff;
    --card-edge: #d6d6d6;
    --sky-deep: #2c4f8e;
    --sky-light: #9fbde0;
    --suit-dark: #1c2233;
  }
  * { box-sizing: border-box; margin: 0; padding: 0; }
  html, body { width: 1200px; height: 800px; overflow: hidden; background: var(--paper); }
  .sheet {
    position: relative; width: 1200px; height: 800px;
    background: var(--paper); font-family: "Arimo", Arial, sans-serif; color: var(--ink);
  }
  .sheet-title {
    position: absolute; top: 26px; left: 0; width: 100%;
    text-align: center; font-size: 29px; font-weight: 700; letter-spacing: 0.3px;
  }
  .card {
    position: absolute; background: var(--paper);
    border: 1px solid var(--card-edge); overflow: hidden;
  }
  .card--portrait { left: 77px; top: 113px; width: 424px; height: 571px; }
  .card--landscape { left: 551px; top: 198px; width: 606px; height: 400px; }
  .script-greeting {
    position: absolute; font-family: "Great Vibes", cursive; font-weight: 400;
    color: var(--ink); white-space: nowrap;
  }
  .card--portrait .script-greeting { top: 27px; left: 0; width: 100%; text-align: center; font-size: 38px; }
  .card--landscape .script-greeting { top: 164px; left: 52px; font-size: 42px; }
  .photo-area {
    position: absolute;
    background: linear-gradient(160deg, var(--sky-deep) 0%, #4f76b4 45%, var(--sky-light) 100%);
  }
  .card--portrait .photo-area { left: 0; top: 97px; width: 424px; height: 240px; }
  .accent-band { position: absolute; left: 0; top: 337px; width: 424px; height: 11px; background: var(--brand-green); }
  .photo-slant { position: absolute; left: 0; top: 0; }
  .brand {
    position: absolute; display: flex; align-items: center; gap: 14px;
  }
  .brand-square { background: var(--brand-green); flex: none; }
  .brand-name {
    font-family: "Carlito", Calibri, sans-serif; font-weight: 400;
    color: var(--brand-green); font-size: 21px; line-height: 21px;
  }
  .card--portrait .brand { left: 12px; top: 493px; }
  .card--portrait .brand-square { width: 62px; height: 65px; }
  .card--landscape .brand { left: 17px; top: 319px; }
  .card--landscape .brand-square { width: 58px; height: 61px; }
  .corner-mark { position: absolute; background: var(--brand-green); }
  .card--portrait .corner-mark--upper { left: 369px; top: 512px; width: 21px; height: 21px; }
  .card--portrait .corner-mark--lower { left: 390px; top: 535px; width: 21px; height: 21px; }
  .card--landscape .corner-mark--upper { left: 548px; top: 351px; width: 17px; height: 17px; }
  .card--landscape .corner-mark--lower { left: 565px; top: 370px; width: 17px; height: 17px; }
  .sample-label { position: absolute; font-size: 15px; text-align: center; width: 160px; }
  .sample-label--one { left: 209px; top: 693px; }
  .sample-label--two { left: 774px; top: 609px; }
</style>
</head>
<body>
<main class="sheet">
  <h1 class="sheet-title">Thank You Card</h1>

  <section class="card card--portrait">
    <p class="script-greeting">Thank You</p>
    <div class="photo-area" role="img" aria-label="Photo of two business people shaking hands against blue sky and office towers"></div>
    <div class="accent-band"></div>
    <div class="brand">
      <span class="brand-square"></span>
      <span class="brand-name">Lanemark<br>Insurance Brokers</span>
    </div>
    <span class="corner-mark corner-mark--upper"></span>
    <span class="corner-mark corner-mark--lower"></span>
  </section>
  <p class="sample-label sample-label--one">Sample 1</p>

  <section class="card card--landscape">
    <svg class="photo-slant" width="606" height="400" viewBox="0 0 606 400">
      <defs>
        <linearGradient id="sky-fill" x1="0" y1="0" x2="1" y2="1">
          <stop offset="0" stop-color="#2c4f8e"/>
          <stop offset="0.5" stop-color="#4f76b4"/>
          <stop offset="1" stop-color="#9fbde0"/>
        </linearGradient>
      </defs>
      <polygon class="slant-band" points="183,0 606,0 606,297 319,273" fill="#9a9a9a"/>
      <polygon class="slant-photo" points="193,0 606,0 606,282 328,262" fill="url(#sky-fill)"
        role="img" aria-label="Photo of two business people shaking hands against blue sky and office towers"/>
    </svg>
    <p class="script-greeting">Thank You</p>
    <div class="brand">
      <span class="brand-square"></span>
      <span class="brand-name">Lanemark<br>Insurance Brokers</span>
    </div>
    <span class="corner-mark corner-mark--upper"></span>
    <span class="corner-mark corner-mark--lower"></span>
  </section>
  <p class="sample-label sample-label--two">Sample 2</p>
</main>
</body>
</html>
```